Real Estate Sales Brokerage

Design a modern and fresh looking standard size business card, incorporate our logo's color scheme and modern appearance with head shot photo on front side and incorporate our log on the back side

Target Market(s)

Residential Home sales

Industry/Entity Type

Real Estate Agent

Font styles to use
Sans Serif

Colors

Designer to choose colors to be used in the design.

Requirements
Must have
• fresh, modern, not too busy, incorporate head shot in front of the card, incorporate logo in front and back of the card. Use logo design scheme as appropriate.
Nice to have
• horizontal and vertical options to compare would be nice.

```html
<!DOCTYPE html>
<html lang="en">
<head>
<meta charset="utf-8">
<title>Harbor Crest Realty – Business Card</title>
<link rel="stylesheet" href="https://fonts.googleapis.com/css2?family=Arimo:wght@400;700&display=swap">
<style>
  :root {
    --stage: #2b2b2b;
    --white: #ffffff;
    --olive: #66653a;
    --olive-light: #7a7948;
    --yellow: #f3d84b;
    --yellow-deep: #eccf3c;
    --photo-top: #e3e6e8;
    --photo-bottom: #2f4c86;
  }
  * { box-sizing: border-box; margin: 0; padding: 0; }
  html, body {
    width: 1200px; height: 911px; overflow: hidden;
    background: var(--stage);
    font-family: "Arimo", Arial, sans-serif;
  }
  .canvas { position: relative; width: 1200px; height: 911px; }

  .card {
    position: absolute;
    width: 540px; height: 309px;
    overflow: hidden;
    box-shadow: 0 10px 24px rgba(0,0,0,.45);
  }

  /* Front */
  .card-front { left: 70px; top: 130px; background: var(--white); }
  .front-band {
    position: absolute; left: 0; right: 0; top: 170px; bottom: 0;
    background: linear-gradient(90deg, var(--olive-light), var(--olive));
    border-top: 6px solid var(--yellow);
  }
  .brand {
    position: absolute; display: flex; align-items: center; gap: 12px;
  }
  .brand-mark { width: 34px; height: 34px; background: var(--olive); flex: none; }
  .brand-name {
    color: var(--olive); font-weight: 400; font-size: 19px;
    line-height: 1.02; letter-spacing: .5px; text-transform: uppercase;
  }
  .card-front .brand { left: 42px; top: 66px; }
  .headshot {
    position: absolute; left: 332px; top: 20px; width: 176px; height: 144px;
    border-radius: 10px;
    background: linear-gradient(160deg, var(--photo-top) 35%, var(--photo-bottom));
  }
  .contact {
    position: absolute; left: 42px; bottom: 24px;
    color: var(--white); font-size: 12.5px; line-height: 1.45;
  }
  .person {
    position: absolute; right: 34px; top: 40px; text-align: right; color: var(--white);
  }
  .person-name { font-weight: 700; font-size: 21px; letter-spacing: .3px; }
  .person-title { font-size: 13px; margin-top: 3px; }

  /* Back */
  .card-back {
    left: 590px; top: 472px;
    background: linear-gradient(135deg, var(--yellow), var(--yellow-deep));
  }
  .website {
    position: absolute; left: 0; right: 0; top: 22px; text-align: center;
    color: var(--white); font-size: 11px; letter-spacing: 5px;
  }
  .card-back .brand { left: 50%; top: 50%; transform: translate(-50%, -50%); gap: 16px; }
  .card-back .brand-mark { width: 58px; height: 58px; background: var(--white); }
  .card-back .brand-name { color: var(--white); font-size: 27px; }
</style>
</head>
<body>
<main class="canvas">

  <section class="card card-front" aria-label="Business card front">
    <div class="brand">
      <span class="brand-mark"></span>
      <span class="brand-name">Harbor<br>Crest<br>Realty</span>
    </div>
    <div class="headshot" role="img" aria-label="Headshot photo of the agent in a blue suit"></div>
    <div class="front-band">
      <address class="contact" style="font-style:normal">
        412 Willow Bend Road<br>
        Juneau, Alaska 99801<br>
        P.555 210 4471 M.555 318 9026<br>
        E.name@harborcrestrealty.com<br>
        www.harborcrestrealty.com
      </address>
      <div class="person">
        <p class="person-name">DANIEL REYES</p>
        <p class="person-title">CEO/FOUNDER</p>
      </div>
    </div>
  </section>

  <section class="card card-back" aria-label="Business card back">
    <p class="website">www.harborcrestrealty.com</p>
    <div class="brand">
      <span class="brand-mark"></span>
      <span class="brand-name">Harbor<br>Crest<br>Realty</span>
    </div>
  </section>

</main>
</body>
</html>
```